luxury contemporary fashion website needs simple, elegant flowchart to describe the buying and selli

* Luxury, resale, preloved items are sold on this online platform
*Horizontal, simple, flowchart with 5 steps in 'friendly' font with a simple emoticon/ picture for each step
*To be positioned in the 'How we work' tab of the webpage to explain in a very simple manner the buying and selling process for the customers.
*Attached is a very rudimentary mock-up of what we would like included and an idea of a project similar to what we desire
* to confirm the text for each step, we have also attached a word file below

Industry/Entity Type

Fashion

Font styles to use
Sans Serif

Colors
86cfc6
cfeae6

Requirements
Must have
• Simple drawing / shape after each point In the closest to 'duck egg blue' fill colour you can find with a black outline

```html
<!DOCTYPE html>
<html lang="en">
<head>
<meta charset="utf-8">
<title>Bespoke Personal Concierge</title>
<link rel="stylesheet" href="https://fonts.googleapis.com/css2?family=Jost:wght@300;400;700&display=swap">
<style>
  :root {
    --teal: #86cfc6;
    --teal-soft: #cfeae6;
    --rule: #a9dbd4;
    --ink: #1a1a1a;
    --body: #333333;
    --paper: #ffffff;
  }
  html, body { margin: 0; padding: 0; overflow: hidden; background: var(--paper); }
  .canvas {
    position: relative;
    width: 1200px;
    height: 300px;
    overflow: hidden;
    background: var(--paper);
    font-family: "Jost", sans-serif;
    color: var(--body);
  }
  .rules { position: absolute; left: 0; top: 0; width: 1200px; height: 60px; }
  .title {
    position: absolute; left: 378px; top: 10px; margin: 0;
    font-weight: 300; font-size: 37px; letter-spacing: 0.3px;
    color: var(--teal); white-space: nowrap;
  }
  .step-heading {
    position: absolute; margin: 0;
    font-weight: 700; font-size: 20px; line-height: 27px;
    color: var(--ink); letter-spacing: 0.3px;
  }
  .step-text {
    position: absolute; margin: 0;
    font-weight: 300; font-size: 16px; line-height: 21.5px;
    color: var(--body);
  }
  .step-text .indent { padding-left: 18px; }
  .step-number {
    position: absolute; top: 248px; margin: 0;
    font-weight: 700; font-size: 31px; color: var(--teal);
  }
  .accent { color: var(--teal); font-weight: 700; }
  .icon { display: inline-block; vertical-align: middle; }
  .payment-flow { position: absolute; left: 715px; top: 95px; width: 300px; height: 140px; }
  .payment-label {
    position: absolute; left: 741px; top: 150px; margin: 0;
    font-weight: 700; font-size: 20px; color: var(--teal); letter-spacing: 0.3px;
  }
  .outcome {
    position: absolute; left: 993px; margin: 0;
    font-weight: 400; font-size: 16px; line-height: 21px; color: var(--ink);
  }
  .currency {
    position: absolute; left: 1120px; top: 96px; margin: 0;
    font-weight: 700; font-size: 11px; color: var(--teal);
  }
</style>
</head>
<body>
<div class="canvas">
  <svg class="rules" viewBox="0 0 1200 60" aria-hidden="true">
    <g stroke="var(--rule)" stroke-width="1.2">
      <line x1="85" y1="18" x2="365" y2="18"/>
      <line x1="150" y1="32" x2="365" y2="32"/>
      <line x1="205" y1="46" x2="365" y2="46"/>
      <line x1="838" y1="25" x2="1118" y2="25"/>
      <line x1="838" y1="38" x2="1053" y2="38"/>
      <line x1="838" y1="52" x2="998" y2="52"/>
    </g>
  </svg>
  <h1 class="title">Bespoke Personal Concierge</h1>

  <!-- Step 1 -->
  <h2 class="step-heading" style="left:65px; top:72px;">Have items<br><span style="padding-left:22px">to sell <span class="accent">?</span></span></h2>
  <p class="step-text" style="left:76px; top:134px;">- brand spanking<br><span class="indent">or nearly</span><br><span class="indent">new</span>
    <svg class="icon" width="12" height="12" viewBox="0 0 12 12" aria-hidden="true"><g fill="var(--teal)"><circle cx="3" cy="4" r="1.4"/><circle cx="8" cy="2.5" r="1.2"/><circle cx="6" cy="8" r="1.5"/></g></svg></p>
  <p class="step-number" style="left:112px;">1</p>

  <!-- Step 2 -->
  <h2 class="step-heading" style="left:233px; top:72px;">Personal<br>collection</h2>
  <p class="step-text" style="left:234px; top:134px;">- we choose the<br><span style="padding-left:12px">pieces we know</span><br><span style="padding-left:12px">the velora</span><br><span style="padding-left:12px">customers</span><br><span style="padding-left:12px">will love</span>
    <svg class="icon" width="17" height="15" viewBox="0 0 20 18" aria-hidden="true"><path d="M10 17 C3 11 1 8 1 5 A4.5 4.5 0 0 1 10 3.5 A4.5 4.5 0 0 1 19 5 C19 8 17 11 10 17Z" fill="var(--teal)"/></svg></p>
  <p class="step-number" style="left:264px;">2</p>

  <!-- Step 3 -->
  <h2 class="step-heading" style="left:380px; top:72px;">We Prepare</h2>
  <p class="step-text" style="left:379px; top:124px; font-size:15.5px;">- your item for sale<br><span style="padding-left:10px">with thorough autheticity</span><br><span style="padding-left:10px">&amp; condition checks...</span><br><span style="padding-left:22px">so&nbsp; you</span><br><span style="padding-left:28px">don't have to !</span>
    <svg class="icon" width="16" height="16" viewBox="0 0 16 16" aria-hidden="true"><circle cx="8" cy="8" r="7.5" fill="var(--teal)"/><circle cx="5.5" cy="6" r="1" fill="#fff"/><circle cx="10.5" cy="6" r="1" fill="#fff"/><path d="M4.5 9.5 Q8 13 11.5 9.5" stroke="#fff" stroke-width="1.3" fill="none"/></svg></p>
  <p class="step-number" style="left:430px;">3</p>

  <!-- Step 4 -->
  <h2 class="step-heading" style="left:548px; top:72px;">Once sold</h2>
  <p class="step-text" style="left:556px; top:134px;">-we lovingly<br><span style="padding-left:12px">prepare the item</span><br><span style="padding-left:8px; line-height:32px">- shipped via</span><br><span style="padding-left:26px; position:relative; top:-8px">tracked services</span>
    <svg class="icon" width="22" height="14" viewBox="0 0 22 14" aria-hidden="true" style="position:relative; top:-8px"><path d="M1 9 L21 3 L13 12 L11 8 Z" fill="var(--teal-soft)" stroke="var(--teal)" stroke-width="1"/><path d="M11 8 L21 3" stroke="var(--teal)" stroke-width="1"/></svg></p>
  <p class="step-number" style="left:600px;">4</p>

  <!-- Step 5 -->
  <svg class="payment-flow" viewBox="0 0 300 140" aria-hidden="true">
    <path d="M30 105 C8 108 4 80 24 74 C10 60 28 38 48 48 C52 26 82 22 94 38 C104 18 138 22 140 44 C162 40 176 60 162 74 C182 84 168 112 146 104 C140 124 108 124 100 108 C88 126 54 124 52 106 C44 112 34 110 30 105 Z"
          fill="none" stroke="var(--teal)" stroke-width="4" stroke-linejoin="round"/>
    <path d="M172 68 C200 48 225 36 255 32" fill="none" stroke="var(--teal)" stroke-width="4" stroke-linecap="round"/>
    <path d="M246 24 L258 32 L246 39" fill="none" stroke="var(--teal)" stroke-width="3" stroke-linecap="round" stroke-linejoin="round"/>
    <path d="M172 84 C200 100 225 108 255 110" fill="none" stroke="var(--teal)" stroke-width="4" stroke-linecap="round"/>
    <path d="M246 103 L258 110 L246 117" fill="none" stroke="var(--teal)" stroke-width="3" stroke-linecap="round" stroke-linejoin="round"/>
  </svg>
  <p class="payment-label">Your payment</p>
  <p class="outcome" style="top:113px;">Pocket the cash</p>
  <p class="currency">£<sub>$</sub><sup>€</sup></p>
  <p class="outcome" style="top:193px;">Donate to charity<br>(full or partial amount)</p>
  <svg class="icon" width="18" height="18" viewBox="0 0 18 18" aria-hidden="true" style="position:absolute; left:1164px; top:206px;"><circle cx="9" cy="9" r="7.5" fill="none" stroke="var(--teal)" stroke-width="1.3"/><path d="M5 7 Q6.2 5.8 7.4 7 M10.6 7 Q11.8 5.8 13 7" stroke="var(--teal)" stroke-width="1.2" fill="none"/><path d="M5.5 10.5 Q9 14 12.5 10.5" stroke="var(--teal)" stroke-width="1.3" fill="none"/></svg>
  <p class="step-number" style="left:820px;">5</p>
</div>
</body>
</html>
```